Alder Hollow Family Dentistry
business card
Alder Hollow Family Dentistry -
Creative Brief
Simple
Dr. Owen T. Farrow, D.M.D.
2817 Juniper Ln. Ste. C Fernwick Falls, NV 84561
drfarrow@alderhollowfamilydentistry.example
www.alderhollowfamilydentistry.example

```html
<!DOCTYPE html>
<html lang="en">
<head>
<meta charset="utf-8">
<title>Alder Hollow Family Dentistry – Business Cards</title>
<link rel="stylesheet" href="https://fonts.googleapis.com/css2?family=Arimo:wght@400;700&display=swap">
<style>
  :root {
    --backdrop: #e9e9eb;
    --green: #2e9a3c;
    --green-light: #5cc04a;
    --green-dark: #1f7e2f;
    --blue: #1f6fc4;
    --blue-light: #3f95e2;
    --blue-dark: #1457a8;
    --white: #ffffff;
    --ink: #222222;
    --name-green: #2a8a36;
  }
  * { margin: 0; padding: 0; box-sizing: border-box; }
  html, body {
    width: 1200px; height: 749px; overflow: hidden;
    background: var(--backdrop);
    font-family: "Arimo", Arial, sans-serif;
  }
  .sheet { position: relative; width: 1200px; height: 749px; }
  .card {
    position: absolute; width: 557px; height: 312px;
    border-radius: 24px; overflow: hidden;
    box-shadow: 0 1px 3px rgba(0,0,0,.18);
  }
  .card--front  { left: 29px;  top: 43px; background: var(--white); }
  .card--green  { left: 614px; top: 43px;
    background: radial-gradient(ellipse at 40% 40%, var(--green-light), var(--green) 60%, var(--green-dark)); }
  .card--blue   { left: 29px;  top: 391px;
    background: radial-gradient(ellipse at 40% 40%, var(--blue-light), var(--blue) 60%, var(--blue-dark)); }
  .card--white  { left: 614px; top: 391px; background: var(--white); }

  .front-shape { position: absolute; inset: 0; }

  .wordmark {
    position: absolute; font-weight: 700; line-height: 1.1;
    text-align: center; color: var(--white);
  }
  .wordmark .line1 { display: block; font-size: 34px; letter-spacing: 1px; }
  .wordmark .line2 { display: block; font-size: 22px; letter-spacing: 1.5px; }

  .card--front .wordmark { left: 34px; top: 36px; text-align: left; }
  .card--front .wordmark .line1 { font-size: 24px; }
  .card--front .wordmark .line2 { font-size: 16px; }

  .card--green .wordmark,
  .card--blue .wordmark,
  .card--white .wordmark { left: 0; right: 0; top: 112px; }
  .card--white .wordmark { color: var(--green-dark); }

  .contact {
    position: absolute; right: 30px; top: 86px;
    text-align: right; color: var(--ink);
    font-size: 12.5px; line-height: 17px;
  }
  .contact .doctor {
    color: var(--name-green); font-weight: 700; font-size: 19px;
    margin-bottom: 34px; line-height: 22px;
  }
  .contact b { font-weight: 700; }

  .web {
    position: absolute; left: 0; right: 0; bottom: 20px;
    text-align: center; font-size: 13px; color: var(--white);
  }
  .web b { font-weight: 700; }
  .card--white .web { color: var(--ink); }
</style>
</head>
<body>
<main class="sheet">

  <section class="card card--front">
    <svg class="front-shape" viewBox="0 0 557 312" width="557" height="312" aria-hidden="true">
      <defs>
        <radialGradient id="frontGreen" cx="30%" cy="35%" r="70%">
          <stop offset="0" stop-color="#5cc04a"/>
          <stop offset="0.6" stop-color="#2e9a3c"/>
          <stop offset="1" stop-color="#1f7e2f"/>
        </radialGradient>
      </defs>
      <rect width="557" height="312" fill="url(#frontGreen)"/>
      <path d="M330 0 C240 60 200 200 120 312 L190 312 C245 210 270 80 345 0 Z" fill="#1f6fc4"/>
      <path d="M345 0 C270 80 245 210 190 312 L557 312 L557 0 Z" fill="#ffffff"/>
    </svg>
    <div class="wordmark">
      <span class="line1">Alder Hollow</span>
      <span class="line2">Family Dentistry</span>
    </div>
    <div class="contact">
      <p class="doctor">Dr. Owen T. Farrow, D.M.D.</p>
      <p>2817 Juniper Ln. Ste. C</p>
      <p>Fernwick Falls, NV 84561</p>
      <p><b>P :</b> 555-014-2290</p>
      <p><b>F :</b> 555-014-2291</p>
      <p><b>E :</b> drfarrow@alderhollowfamilydentistry.example</p>
      <p><b>W :</b> www.alderhollowfamilydentistry.example</p>
    </div>
  </section>

  <section class="card card--green">
    <div class="wordmark">
      <span class="line1">Alder Hollow</span>
      <span class="line2">Family Dentistry</span>
    </div>
    <p class="web"><b>www.alderhollowfamilydentistry</b>.example</p>
  </section>

  <section class="card card--blue">
    <div class="wordmark">
      <span class="line1">Alder Hollow</span>
      <span class="line2">Family Dentistry</span>
    </div>
    <p class="web"><b>www.alderhollowfamilydentistry</b>.example</p>
  </section>

  <section class="card card--white">
    <div class="wordmark">
      <span class="line1">Alder Hollow</span>
      <span class="line2">Family Dentistry</span>
    </div>
    <p class="web"><b>www.alderhollowfamilydentistry</b>.example</p>
  </section>

</main>
</body>
</html>
```